CAR PAINT AEROSOL

car paint aerosol
3 different aerosols
x1 paint
x1 lacquer
x1 primer

We want something eye catching that will outshine competitors this is automotive paint, we are looking for something modern and clean. Will require a logo as well as the can design too. We have added our 'KMV' brand that is already competitive on the market but this looks very 'trade' style so looking for something more retail (will attach photos of our current aerosols) . Please note we are looking for a new brand name, logo and design. So a completely different brand and look to our current KMV aerosols.
examples of competitors attached

label template attached

Target Market(s)

AUTOMOTIVE INDUSTRY TO RETAIL BUYERS,

Industry/Entity Type

car paint

Requirements
Must have
• NEW BRAND NAME , LOGO AND DESIGN
Nice to have
• own domain www.glenvarnish.co.uk not essential to design but would be good for brand to tie in
Should not have
• ideally not red as current brand is

```html
<!DOCTYPE html>
<html lang="en">
<head>
<meta charset="utf-8">
<title>Glenvarnish Aerosol Label Range</title>
<link rel="stylesheet" href="https://fonts.googleapis.com/css2?family=Arimo:wght@400;700&family=Montserrat:ital,wght@1,900&display=swap">
<style>
  :root {
    --ink: #000000;
    --paper: #ffffff;
    --trim: #e0202a;
    --lime: #d6e600;
    --cyan: #14bde6;
    --magenta: #c61fc0;
    --red: #de3338;
    --green: #33cc33;
    --orange: #ff7a00;
    --violet: #5c5cf6;
  }
  * { box-sizing: border-box; margin: 0; padding: 0; }
  html, body { width: 1200px; height: 875px; overflow: hidden; background: var(--paper); }
  body { position: relative; font-family: "Arimo", Arial, sans-serif; }

  .label {
    position: absolute; width: 347px; height: 251px;
    background: var(--ink); overflow: hidden; color: var(--paper);
  }
  .label--paint { left: 42px; top: 43px; --accent: var(--lime); }
  .label--primer { left: 426px; top: 43px; --accent: var(--cyan); }
  .label--lacquer { left: 811px; top: 43px; --accent: var(--magenta); }
  .label--etch { left: 42px; top: 312px; --accent: var(--red); }
  .label--isolator { left: 426px; top: 312px; --accent: var(--green); }
  .label--plastic { left: 811px; top: 312px; --accent: var(--orange); }
  .label--clear { left: 42px; top: 580px; --accent: var(--violet); }

  .band-top { position: absolute; left: 0; top: 0; width: 100%; height: 10px; background: var(--accent); }
  .band-bottom { position: absolute; left: 0; bottom: 0; width: 100%; height: 21px; background: var(--accent); }
  .seam { position: absolute; top: 0; width: 3px; height: 10px; background: var(--ink); transform: skewX(-14deg); }
  .seam--a { left: 234px; } .seam--b { left: 258px; }
  .trim-line { position: absolute; inset: 4px; border: 0.6px solid var(--trim); border-radius: 3px; z-index: 5; pointer-events: none; }

  .spray-field {
    position: absolute; left: 143px; top: 132px; width: 204px; height: 98px;
    background:
      radial-gradient(ellipse 55% 70% at 80% 100%, var(--accent) 0%, transparent 75%),
      radial-gradient(ellipse 60% 80% at 20% 100%, var(--accent) 0%, transparent 70%);
    opacity: 0.75;
  }

  .brand {
    position: absolute; left: 176px; top: 20px; width: 160px; text-align: center;
    font-weight: 700; font-size: 12px; letter-spacing: 0.5px; color: var(--paper);
  }

  .product-name {
    position: absolute; top: 40px; bottom: 32px;
    writing-mode: vertical-rl; transform: rotate(180deg); text-align: start;
    font-family: "Montserrat", sans-serif; font-style: italic; font-weight: 900;
    color: var(--paper); line-height: 0.92; white-space: nowrap; overflow: hidden;
  }
  .product-name--paint { left: 232px; font-size: 44px; text-transform: uppercase; }
  .product-name--primer { left: 234px; font-size: 40px; text-transform: uppercase; }
  .product-name--lacquer { left: 236px; font-size: 34px; text-transform: uppercase; }
  .product-name--double { left: 212px; font-size: 39px; }
  .product-name--long { left: 214px; font-size: 35px; }

  .volume { position: absolute; left: 230px; bottom: 6px; width: 44px; text-align: center; font-weight: 700; font-size: 8px; color: var(--ink); }

  .tech-panel { position: absolute; left: 16px; top: 14px; width: 123px; }
  .range-tag {
    background: var(--paper); color: var(--ink); height: 24px; border-radius: 3px 3px 0 0;
    padding: 2px 4px; font-size: 8.4px; line-height: 1.2;
  }
  .panel-heading { font-size: 5.4px; margin: 3px 0 2px 3px; }
  .panel-copy { font-size: 2.9px; line-height: 1.3; margin-left: 3px; }
  .panel-rule { border-top: 0.6px solid var(--paper); margin: 3px 0 0 2px; }

  .hazards { position: absolute; left: 30px; top: 131px; display: flex; gap: 4px; }
  .hazards svg { width: 38px; height: 38px; }

  .info-box {
    position: absolute; left: 16px; top: 169px; width: 123px; height: 68px;
    background: var(--paper); color: var(--ink); border-radius: 0 0 5px 5px; padding: 3px 4px;
  }
  .mark-row { display: flex; align-items: center; justify-content: space-between; height: 14px; }
  .voc { border: 0.8px solid var(--ink); font-weight: 700; font-size: 6px; padding: 0 1px; }
  .tick { font-size: 8px; font-weight: 700; margin-left: 1px; }
  .reg-note { font-size: 3px; text-align: right; line-height: 1.2; }
  .icon-row { display: flex; align-items: center; justify-content: space-between; height: 18px; }
  .recycle { font-size: 9px; line-height: 1; }
  .code-box { border: 0.6px solid var(--ink); font-size: 4.5px; padding: 0 1px; }
  .abuse { font-size: 3.4px; line-height: 1.1; text-align: center; font-weight: 700; }
  .e-mark { font-size: 11px; }
  .ukca { font-size: 5.5px; font-weight: 700; line-height: 0.95; }
  .address { font-size: 3px; line-height: 1.25; margin-top: 3px; }
  .foot-row { display: flex; justify-content: space-between; align-items: baseline; margin-top: 2px; }
  .ufi { font-size: 3px; }
  .net { font-size: 6.5px; }
</style>
</head>
<body>

<svg width="0" height="0" style="position:absolute" aria-hidden="true">
  <defs>
    <symbol id="hazard-exclaim" viewBox="0 0 40 40">
      <rect x="8" y="8" width="24" height="24" transform="rotate(45 20 20)" fill="#fff" stroke="#e0202a" stroke-width="3"/>
      <rect x="18.3" y="10.5" width="3.4" height="12" rx="1.2" fill="#000"/>
      <circle cx="20" cy="27" r="2" fill="#000"/>
    </symbol>
    <symbol id="hazard-flame" viewBox="0 0 40 40">
      <rect x="8" y="8" width="24" height="24" transform="rotate(45 20 20)" fill="#fff" stroke="#e0202a" stroke-width="3"/>
      <path d="M20 10 C23 15 26 17 25 22 C24.5 25 22 26.5 20 26.5 C17.5 26.5 15 25 15 22 C15 19 17 18 17.5 16 C18.5 18 19 19 20 19 C20.5 16 19.5 13 20 10 Z" fill="#000"/>
      <rect x="13" y="27.5" width="14" height="1.8" fill="#000"/>
    </symbol>
  </defs>
</svg>

<section class="label label--paint">
  <div class="band-top"></div><span class="seam seam--a"></span><span class="seam seam--b"></span>
  <div class="spray-field" role="img" aria-label="Halftone spray dot pattern in lime"></div>
  <div class="brand">GLENVARNISH.CO.UK</div>
  <div class="product-name product-name--paint">Paint</div>
  <div class="tech-panel">
    <div class="range-tag">ULTRA<br>ATOMISER</div>
    <p class="panel-heading">DIRECTIONS</p>
    <p class="panel-copy">1. The surface must be clean, dry and dust-free<br>2. Shake aerosol for at least two minutes, after the agitator ball is free<br>3. Apply in cross coats from distance of 250mm from object<br>4. Drying time: 10 - 20 minutes<br>5. After use turn aerosol upside down empty valve</p>
    <div class="panel-rule"></div>
    <p class="panel-heading">WARNING</p>
    <p class="panel-copy">Danger. Extremely flammable aerosol. Pressurised container: may burst if heated. Causes serious eye irritation. May cause drowsiness or dizziness. Keep out of reach of children. Keep away from heat, hot surfaces, sparks, open flames and other ignition sources. No smoking. Do not spray on an open flame. Do not pierce or burn, even after use. Do not breathe spray. Protect from sunlight. Dispose of contents in accordance with regional regulations. Use only with sufficient ventilation. Contains: acetone, n-butyl acetate.</p>
  </div>
  <div class="hazards"><svg><use href="#hazard-exclaim"/></svg><svg><use href="#hazard-flame"/></svg></div>
  <div class="info-box">
    <div class="mark-row"><span class="voc">VOC</span><span class="tick">✓</span><span style="flex:1"></span><span class="reg-note">2004/42/IIB(e),<br>VOC max. 840g/l,<br>VOC 711.0 g/l</span></div>
    <div class="icon-row"><span class="recycle">♻</span><span class="code-box">520</span><span class="abuse">SOLVENT<br>ABUSE<br>CAN KILL<br>INSTANTLY</span><span class="e-mark">℮3</span><span class="ukca">UK<br>CA</span></div>
    <p class="address">Address Line 1<br>Address Line 2<br>Town, Country, Postcode<br>W: www.glenvarnish.co.uk</p>
    <div class="foot-row"><span class="ufi">UFI code: 4KP1-9WXR-2210-HM5D</span><span class="net">400ml</span></div>
  </div>
  <div class="band-bottom"></div>
  <div class="volume">400ml</div>
  <div class="trim-line"></div>
</section>

<section class="label label--primer">
  <div class="band-top"></div><span class="seam seam--a"></span><span class="seam seam--b"></span>
  <div class="spray-field" role="img" aria-label="Halftone spray dot pattern in cyan"></div>
  <div class="brand">GLENVARNISH.CO.UK</div>
  <div class="product-name product-name--primer">Primer</div>
  <div class="tech-panel">
    <div class="range-tag">ULTRA<br>ATOMISER</div>
    <p class="panel-heading">DIRECTIONS</p>
    <p class="panel-copy">1. The surface must be clean, dry and dust-free<br>2. Shake aerosol for at least two minutes, after the agitator ball is free<br>3. Apply in cross coats from distance of 250mm from object<br>4. Drying time: 10 - 20 minutes<br>5. After use turn aerosol upside down empty valve</p>
    <div class="panel-rule"></div>
    <p class="panel-heading">WARNING</p>
    <p class="panel-copy">Danger. Extremely flammable aerosol. Pressurised container: may burst if heated. Causes serious eye irritation. May cause drowsiness or dizziness. Keep out of reach of children. Keep away from heat, hot surfaces, sparks, open flames and other ignition sources. No smoking. Do not spray on an open flame. Do not pierce or burn, even after use. Do not breathe spray. Protect from sunlight. Dispose of contents in accordance with regional regulations. Use only with sufficient ventilation. Contains: acetone, n-butyl acetate.</p>
  </div>
  <div class="hazards"><svg><use href="#hazard-exclaim"/></svg><svg><use href="#hazard-flame"/></svg></div>
  <div class="info-box">
    <div class="mark-row"><span class="voc">VOC</span><span class="tick">✓</span><span style="flex:1"></span><span class="reg-note">2004/42/IIB(e),<br>VOC max. 840g/l,<br>VOC 711.0 g/l</span></div>
    <div class="icon-row"><span class="recycle">♻</span><span class="code-box">520</span><span class="abuse">SOLVENT<br>ABUSE<br>CAN KILL<br>INSTANTLY</span><span class="e-mark">℮3</span><span class="ukca">UK<br>CA</span></div>
    <p class="address">Address Line 1<br>Address Line 2<br>Town, Country, Postcode<br>W: www.glenvarnish.co.uk</p>
    <div class="foot-row"><span class="ufi">UFI code: 4KP1-9WXR-2210-HM5D</span><span class="net">400ml</span></div>
  </div>
  <div class="band-bottom"></div>
  <div class="volume">500ml</div>
  <div class="trim-line"></div>
</section>

<section class="label label--lacquer">
  <div class="band-top"></div><span class="seam seam--a"></span><span class="seam seam--b"></span>
  <div class="spray-field" role="img" aria-label="Halftone spray dot pattern in magenta"></div>
  <div class="brand">GLENVARNISH.CO.UK</div>
  <div class="product-name product-name--lacquer">Lacquer</div>
  <div class="tech-panel">
    <div class="range-tag">ULTRA<br>ATOMISER</div>
    <p class="panel-heading">DIRECTIONS</p>
    <p class="panel-copy">1. The surface must be clean, dry and dust-free<br>2. Shake aerosol for at least two minutes, after the agitator ball is free<br>3. Apply in cross coats from distance of 250mm from object<br>4. Drying time: 10 - 20 minutes<br>5. After use turn aerosol upside down empty valve</p>
    <div class="panel-rule"></div>
    <p class="panel-heading">WARNING</p>
    <p class="panel-copy">Danger. Extremely flammable aerosol. Pressurised container: may burst if heated. Causes serious eye irritation. May cause drowsiness or dizziness. Keep out of reach of children. Keep away from heat, hot surfaces, sparks, open flames and other ignition sources. No smoking. Do not spray on an open flame. Do not pierce or burn, even after use. Do not breathe spray. Protect from sunlight. Dispose of contents in accordance with regional regulations. Use only with sufficient ventilation. Contains: acetone, n-butyl acetate.</p>
  </div>
  <div class="hazards"><svg><use href="#hazard-exclaim"/></svg><svg><use href="#hazard-flame"/></svg></div>
  <div class="info-box">
    <div class="mark-row"><span class="voc">VOC</span><span class="tick">✓</span><span style="flex:1"></span><span class="reg-note">2004/42/IIB(e),<br>VOC max. 840g/l,<br>VOC 711.0 g/l</span></div>
    <div class="icon-row"><span class="recycle">♻</span><span class="code-box">520</span><span class="abuse">SOLVENT<br>ABUSE<br>CAN KILL<br>INSTANTLY</span><span class="e-mark">℮3</span><span class="ukca">UK<br>CA</span></div>
    <p class="address">Address Line 1<br>Address Line 2<br>Town, Country, Postcode<br>W: www.glenvarnish.co.uk</p>
    <div class="foot-row"><span class="ufi">UFI code: 4KP1-9WXR-2210-HM5D</span><span class="net">400ml</span></div>
  </div>
  <div class="band-bottom"></div>
  <div class="volume">500ml</div>
  <div class="trim-line"></div>
</section>

<section class="label label--etch">
  <div class="band-top"></div><span class="seam seam--a"></span><span class="seam seam--b"></span>
  <div class="spray-field" role="img" aria-label="Halftone spray dot pattern in red"></div>
  <div class="brand">GLENVARNISH.CO.UK</div>
  <div class="product-name product-name--double">Etch<br>Primer</div>
  <div class="tech-panel">
    <div class="range-tag">ULTRA<br>ATOMISER</div>
    <p class="panel-heading">DIRECTIONS</p>
    <p class="panel-copy">1. The surface must be clean, dry and dust-free<br>2. Shake aerosol for at least two minutes, after the agitator ball is free<br>3. Apply in cross coats from distance of 250mm from object<br>4. Drying time: 10 - 20 minutes<br>5. After use turn aerosol upside down empty valve</p>
    <div class="panel-rule"></div>
    <p class="panel-heading">WARNING</p>
    <p class="panel-copy">Danger. Extremely flammable aerosol. Pressurised container: may burst if heated. Causes serious eye irritation. May cause drowsiness or dizziness. Keep out of reach of children. Keep away from heat, hot surfaces, sparks, open flames and other ignition sources. No smoking. Do not spray on an open flame. Do not pierce or burn, even after use. Do not breathe spray. Protect from sunlight. Dispose of contents in accordance with regional regulations. Use only with sufficient ventilation. Contains: acetone, n-butyl acetate.</p>
  </div>
  <div class="hazards"><svg><use href="#hazard-exclaim"/></svg><svg><use href="#hazard-flame"/></svg></div>
  <div class="info-box">
    <div class="mark-row"><span class="voc">VOC</span><span class="tick">✓</span><span style="flex:1"></span><span class="reg-note">2004/42/IIB(e),<br>VOC max. 840g/l,<br>VOC 711.0 g/l</span></div>
    <div class="icon-row"><span class="recycle">♻</span><span class="code-box">520</span><span class="abuse">SOLVENT<br>ABUSE<br>CAN KILL<br>INSTANTLY</span><span class="e-mark">℮3</span><span class="ukca">UK<br>CA</span></div>
    <p class="address">Address Line 1<br>Address Line 2<br>Town, Country, Postcode<br>W: www.glenvarnish.co.uk</p>
    <div class="foot-row"><span class="ufi">UFI code: 4KP1-9WXR-2210-HM5D</span><span class="net">400ml</span></div>
  </div>
  <div class="band-bottom"></div>
  <div class="volume">400ml</div>
  <div class="trim-line"></div>
</section>

<section class="label label--isolator">
  <div class="band-top"></div><span class="seam seam--a"></span><span class="seam seam--b"></span>
  <div class="spray-field" role="img" aria-label="Halftone spray dot pattern in green"></div>
  <div class="brand">GLENVARNISH.CO.UK</div>
  <div class="product-name product-name--double">Paint<br>Isolator</div>
  <div class="tech-panel">
    <div class="range-tag">ULTRA<br>ATOMISER</div>
    <p class="panel-heading">DIRECTIONS</p>
    <p class="panel-copy">1. The surface must be clean, dry and dust-free<br>2. Shake aerosol for at least two minutes, after the agitator ball is free<br>3. Apply in cross coats from distance of 250mm from object<br>4. Drying time: 10 - 20 minutes<br>5. After use turn aerosol upside down empty valve</p>
    <div class="panel-rule"></div>
    <p class="panel-heading">WARNING</p>
    <p class="panel-copy">Danger. Extremely flammable aerosol. Pressurised container: may burst if heated. Causes serious eye irritation. May cause drowsiness or dizziness. Keep out of reach of children. Keep away from heat, hot surfaces, sparks, open flames and other ignition sources. No smoking. Do not spray on an open flame. Do not pierce or burn, even after use. Do not breathe spray. Protect from sunlight. Dispose of contents in accordance with regional regulations. Use only with sufficient ventilation. Contains: acetone, n-butyl acetate.</p>
  </div>
  <div class="hazards"><svg><use href="#hazard-exclaim"/></svg><svg><use href="#hazard-flame"/></svg></div>
  <div class="info-box">
    <div class="mark-row"><span class="voc">VOC</span><span class="tick">✓</span><span style="flex:1"></span><span class="reg-note">2004/42/IIB(e),<br>VOC max. 840g/l,<br>VOC 711.0 g/l</span></div>
    <div class="icon-row"><span class="recycle">♻</span><span class="code-box">520</span><span class="abuse">SOLVENT<br>ABUSE<br>CAN KILL<br>INSTANTLY</span><span class="e-mark">℮3</span><span class="ukca">UK<br>CA</span></div>
    <p class="address">Address Line 1<br>Address Line 2<br>Town, Country, Postcode<br>W: www.glenvarnish.co.uk</p>
    <div class="foot-row"><span class="ufi">UFI code: 4KP1-9WXR-2210-HM5D</span><span class="net">400ml</span></div>
  </div>
  <div class="band-bottom"></div>
  <div class="volume">500ml</div>
  <div class="trim-line"></div>
</section>

<section class="label label--plastic">
  <div class="band-top"></div><span class="seam seam--a"></span><span class="seam seam--b"></span>
  <div class="spray-field" role="img" aria-label="Halftone spray dot pattern in orange"></div>
  <div class="brand">GLENVARNISH.CO.UK</div>
  <div class="product-name product-name--double">Plastic<br>Primer</div>
  <div class="tech-panel">
    <div class="range-tag">ULTRA<br>ATOMISER</div>
    <p class="panel-heading">DIRECTIONS</p>
    <p class="panel-copy">1. The surface must be clean, dry and dust-free<br>2. Shake aerosol for at least two minutes, after the agitator ball is free<br>3. Apply in cross coats from distance of 250mm from object<br>4. Drying time: 10 - 20 minutes<br>5. After use turn aerosol upside down empty valve</p>
    <div class="panel-rule"></div>
    <p class="panel-heading">WARNING</p>
    <p class="panel-copy">Danger. Extremely flammable aerosol. Pressurised container: may burst if heated. Causes serious eye irritation. May cause drowsiness or dizziness. Keep out of reach of children. Keep away from heat, hot surfaces, sparks, open flames and other ignition sources. No smoking. Do not spray on an open flame. Do not pierce or burn, even after use. Do not breathe spray. Protect from sunlight. Dispose of contents in accordance with regional regulations. Use only with sufficient ventilation. Contains: acetone, n-butyl acetate.</p>
  </div>
  <div class="hazards"><svg><use href="#hazard-exclaim"/></svg><svg><use href="#hazard-flame"/></svg></div>
  <div class="info-box">
    <div class="mark-row"><span class="voc">VOC</span><span class="tick">✓</span><span style="flex:1"></span><span class="reg-note">2004/42/IIB(e),<br>VOC max. 840g/l,<br>VOC 711.0 g/l</span></div>
    <div class="icon-row"><span class="recycle">♻</span><span class="code-box">520</span><span class="abuse">SOLVENT<br>ABUSE<br>CAN KILL<br>INSTANTLY</span><span class="e-mark">℮3</span><span class="ukca">UK<br>CA</span></div>
    <p class="address">Address Line 1<br>Address Line 2<br>Town, Country, Postcode<br>W: www.glenvarnish.co.uk</p>
    <div class="foot-row"><span class="ufi">UFI code: 4KP1-9WXR-2210-HM5D</span><span class="net">400ml</span></div>
  </div>
  <div class="band-bottom"></div>
  <div class="volume">500ml</div>
  <div class="trim-line"></div>
</section>

<section class="label label--clear">
  <div class="band-top"></div><span class="seam seam--a"></span><span class="seam seam--b"></span>
  <div class="spray-field" role="img" aria-label="Halftone spray dot pattern in violet"></div>
  <div class="brand">GLENVARNISH.CO.UK</div>
  <div class="product-name product-name--long">2K Clear<br>Lacquer</div>
  <div class="tech-panel">
    <div class="range-tag">ULTRA<br>ATOMISER</div>
    <p class="panel-heading">DIRECTIONS</p>
    <p class="panel-copy">1. The surface must be clean, dry and dust-free<br>2. Shake aerosol for at least two minutes, after the agitator ball is free<br>3. Apply in cross coats from distance of 250mm from object<br>4. Drying time: 10 - 20 minutes<br>5. After use turn aerosol upside down empty valve</p>
    <div class="panel-rule"></div>
    <p class="panel-heading">WARNING</p>
    <p class="panel-copy">Danger. Extremely flammable aerosol. Pressurised container: may burst if heated. Causes serious eye irritation. May cause drowsiness or dizziness. Keep out of reach of children. Keep away from heat, hot surfaces, sparks, open flames and other ignition sources. No smoking. Do not spray on an open flame. Do not pierce or burn, even after use. Do not breathe spray. Protect from sunlight. Dispose of contents in accordance with regional regulations. Use only with sufficient ventilation. Contains: acetone, n-butyl acetate.</p>
  </div>
  <div class="hazards"><svg><use href="#hazard-exclaim"/></svg><svg><use href="#hazard-flame"/></svg></div>
  <div class="info-box">
    <div class="mark-row"><span class="voc">VOC</span><span class="tick">✓</span><span style="flex:1"></span><span class="reg-note">2004/42/IIB(e),<br>VOC max. 840g/l,<br>VOC 711.0 g/l</span></div>
    <div class="icon-row"><span class="recycle">♻</span><span class="code-box">520</span><span class="abuse">SOLVENT<br>ABUSE<br>CAN KILL<br>INSTANTLY</span><span class="e-mark">℮3</span><span class="ukca">UK<br>CA</span></div>
    <p class="address">Address Line 1<br>Address Line 2<br>Town, Country, Postcode<br>W: www.glenvarnish.co.uk</p>
    <div class="foot-row"><span class="ufi">UFI code: 4KP1-9WXR-2210-HM5D</span><span class="net">400ml</span></div>
  </div>
  <div class="band-bottom"></div>
  <div class="volume">400ml</div>
  <div class="trim-line"></div>
</section>

</body>
</html>
```